Business Card Design for Venture Kite

Venture Kite is a pro bono student consultancy service offered by Corvala KTRB to social start ups and enterprises. We provide consulting services with expertise in areas such as Marketing, IT, Business Strategy and Innovation.
I have attached\ the Venture Kite Logo here for your perusal.
Industry/Entity Type
Business
Contact Information for Business Card
Name: Ha Min Park Name: Thomas Leung
Role: Project Leader Role: Vice Project Leader
M:0477203941 M: 0479352806
E: ha-min.park@corvalaktrb.org E: thomas.leung@corvalaktrb.org
W: www.corvalaktrb.org W: www.corvalaktrb.org

```html
<!DOCTYPE html>
<html lang="en">
<head>
<meta charset="utf-8">
<title>Venture Kite Business Cards</title>
<link href="https://fonts.googleapis.com/css2?family=Oswald:wght@400;500;700&display=swap" rel="stylesheet">
<style>
  :root {
    --ink: #0d0d0d;
    --paper: #ffffff;
    --gold: #f2a81d;
    --backdrop: #e6e3de;
    --muted: #d9d9d9;
  }
  * { margin: 0; padding: 0; box-sizing: border-box; }
  html, body { width: 1200px; height: 858px; overflow: hidden; }
  body {
    background: var(--backdrop);
    font-family: "Oswald", "Arial Narrow", sans-serif;
    position: relative;
  }
  .card {
    position: absolute;
    width: 620px;
    height: 354px;
    left: 290px;
    background: var(--paper);
    box-shadow: 0 10px 30px rgba(0,0,0,0.18);
    overflow: hidden;
    display: flex;
  }
  .card--back { top: 48px; }
  .card--front { top: 456px; }

  /* Back card */
  .brand-panel {
    width: 40%;
    display: flex;
    align-items: center;
    justify-content: center;
  }
  .brand-name {
    font-weight: 700;
    font-size: 44px;
    letter-spacing: 1px;
    text-transform: uppercase;
    color: var(--ink);
    line-height: 1;
    text-align: center;
  }
  .contact-panel {
    width: 60%;
    background: var(--ink);
    border-left: 4px solid var(--paper);
    outline: 2px solid var(--ink);
    padding: 42px 36px;
    display: flex;
    flex-direction: column;
    justify-content: space-between;
  }
  .contact-name {
    color: var(--paper);
    font-weight: 500;
    font-size: 30px;
    text-transform: uppercase;
    line-height: 1;
  }
  .contact-role {
    color: var(--gold);
    font-size: 16px;
    text-transform: uppercase;
    letter-spacing: 0.5px;
    margin: 4px 0 10px;
  }
  .contact-line {
    display: flex;
    align-items: center;
    gap: 12px;
    color: var(--paper);
    font-size: 17px;
    margin-top: 6px;
  }
  .contact-icon { width: 20px; height: 18px; flex: none; }

  /* Front card */
  .web-strip {
    width: 16%;
    background: var(--ink);
    display: flex;
    align-items: center;
    justify-content: center;
  }
  .web-address {
    color: var(--gold);
    font-size: 24px;
    letter-spacing: 1px;
    writing-mode: vertical-rl;
    white-space: nowrap;
  }
  .front-panel {
    flex: 1;
    display: flex;
    align-items: center;
    justify-content: center;
  }
  .front-panel .brand-name { font-size: 72px; }
</style>
</head>
<body>

<section class="card card--back">
  <div class="brand-panel">
    <p class="brand-name">Venture<br>Kite</p>
  </div>
  <div class="contact-panel">
    <div class="contact">
      <h2 class="contact-name">Ha Min Park</h2>
      <p class="contact-role">Project Leader</p>
      <p class="contact-line">
        <svg class="contact-icon" viewBox="0 0 20 18"><rect width="20" height="18" fill="#f2a81d"/><path d="M5 4 l3 0 l1 3 l-2 1.5 q1.5 3 4 4 l1.5 -2 l3 1 l0 3 q-8 0 -10.5 -10.5z" fill="#0d0d0d"/></svg>
        0477203941
      </p>
      <p class="contact-line">
        <svg class="contact-icon" viewBox="0 0 20 18"><rect width="20" height="18" fill="#f2a81d"/><rect x="3.5" y="4" width="13" height="10" fill="none" stroke="#0d0d0d" stroke-width="1.5"/><path d="M3.5 4 L10 10 L16.5 4 M3.5 14 L8 9 M16.5 14 L12 9" fill="none" stroke="#0d0d0d" stroke-width="1.5"/></svg>
        ha-min.park@corvalaktrb.org
      </p>
    </div>
    <div class="contact">
      <h2 class="contact-name">Thomas Leung</h2>
      <p class="contact-role">Vice Project Leader</p>
      <p class="contact-line">
        <svg class="contact-icon" viewBox="0 0 20 18"><rect width="20" height="18" fill="#f2a81d"/><path d="M5 4 l3 0 l1 3 l-2 1.5 q1.5 3 4 4 l1.5 -2 l3 1 l0 3 q-8 0 -10.5 -10.5z" fill="#0d0d0d"/></svg>
        0479352806
      </p>
      <p class="contact-line">
        <svg class="contact-icon" viewBox="0 0 20 18"><rect width="20" height="18" fill="#f2a81d"/><rect x="3.5" y="4" width="13" height="10" fill="none" stroke="#0d0d0d" stroke-width="1.5"/><path d="M3.5 4 L10 10 L16.5 4 M3.5 14 L8 9 M16.5 14 L12 9" fill="none" stroke="#0d0d0d" stroke-width="1.5"/></svg>
        thomas.leung@corvalaktrb.org
      </p>
    </div>
  </div>
</section>

<section class="card card--front">
  <div class="web-strip">
    <p class="web-address">www.corvalaktrb.org</p>
  </div>
  <div class="front-panel">
    <p class="brand-name">Venture<br>Kite</p>
  </div>
</section>

</body>
</html>
```